Adult toys brand needs a Packaging Design

- We need design for packaging for Adult Toys brand.
- Packaging is for vibrators.
- Design needs to be clean and modern, minimal
- Main color is white and purple.
- Brand name is VELMO, logo is attached.
- Dielines are attached. The packaging consists of the box and the sleeve that goes on the box. We need design for sleeve ONLY.
Updates

Industry/Entity Type

Adult

Font styles to use
Sans Serif

Requirements
Must have
• - Logo
• - item picture (purple version)
• - web address (velmo.example or www.velmo.example)
• - main features

```html
<!DOCTYPE html>
<html lang="en">
<head>
<meta charset="utf-8">
<title>VELMO Rabbit Vibe – Sleeve</title>
<link rel="stylesheet" href="https://fonts.googleapis.com/css2?family=Quicksand:wght@300;400;700&family=Raleway:wght@300;400&display=swap">
<style>
  :root {
    --plum: #6b3a60;
    --plum-dark: #4e2546;
    --plum-light: #7a4670;
    --product: #5f4470;
    --product-light: #7a628a;
    --ink-grey: #5a5a5a;
    --soft-grey: #7a7a7a;
    --paper: #ffffff;
    --stage: #ececec;
    --line-art: #ece4ec;
  }
  * { box-sizing: border-box; margin: 0; padding: 0; }
  html, body { width: 1200px; height: 1200px; overflow: hidden; }
  body {
    background: var(--stage);
    font-family: "Raleway", sans-serif;
    position: relative;
  }
  .sleeve {
    position: absolute;
    left: 230px; top: 100px;
    width: 740px; height: 1000px;
    display: flex;
    box-shadow: 0 20px 40px rgba(0,0,0,0.12);
  }
  /* Side panel */
  .side-panel {
    width: 220px; height: 100%;
    background: linear-gradient(180deg, var(--plum-dark) 0%, var(--plum) 40%, var(--plum-light) 100%);
    color: var(--paper);
    position: relative;
  }
  .side-brand {
    position: absolute; top: 120px; width: 100%;
    text-align: center;
    font-family: "Quicksand", sans-serif; font-weight: 700;
    font-size: 46px; color: var(--paper);
  }
  .feature {
    position: absolute; left: 0; width: 100%;
    display: flex; flex-direction: column; align-items: center;
  }
  .feature svg { width: 62px; height: 62px; }
  .feature-label {
    margin-top: 10px;
    font-size: 10px; letter-spacing: 1px; text-align: center;
    line-height: 1.4; text-transform: uppercase; opacity: 0.9;
  }
  .feature--ergonomic { top: 280px; }
  .feature--quiet { top: 490px; }
  .feature--waterproof { top: 700px; }
  .feature--luxurious { top: 880px; }

  /* Front panel */
  .front-panel {
    width: 520px; height: 100%;
    background: var(--paper);
    position: relative;
  }
  .brand-name {
    position: absolute; top: 120px; width: 100%;
    text-align: center;
    font-family: "Quicksand", sans-serif; font-weight: 700;
    font-size: 108px; color: var(--ink-grey); letter-spacing: 1px;
  }
  .product-type {
    position: absolute; top: 262px; width: 100%;
    text-align: center;
    font-family: "Raleway", sans-serif; font-weight: 400;
    font-size: 28px; color: var(--soft-grey);
  }
  .illustration-area {
    position: absolute; left: 40px; top: 440px;
    width: 170px; height: 330px;
    background: var(--line-art); border-radius: 80px 80px 30px 30px;
  }
  .product-image {
    position: absolute; left: 160px; top: 350px;
    width: 140px; height: 570px;
    border-radius: 70px 70px 60px 60px;
    background: linear-gradient(180deg, var(--product-light) 0%, var(--product) 60%, #e9e6ea 88%, #ffffff 100%);
  }
  .tagline {
    position: absolute; left: 430px; top: 880px;
    transform: rotate(-90deg); transform-origin: left top;
    white-space: nowrap;
    font-family: "Raleway", sans-serif; font-weight: 300;
    font-size: 50px; color: var(--soft-grey);
  }
  .tagline-accent { color: var(--plum); font-weight: 400; }
  .web-band {
    position: absolute; left: 70px; top: 900px;
    width: 380px; height: 62px;
    background: var(--plum);
    color: var(--paper);
    display: flex; align-items: center; justify-content: center;
    font-family: "Raleway", sans-serif; font-size: 26px; font-weight: 400;
  }
</style>
</head>
<body>
  <div class="sleeve">
    <aside class="side-panel">
      <div class="side-brand">velmo</div>

      <div class="feature feature--ergonomic">
        <svg viewBox="0 0 62 62" fill="none" stroke="#fff" stroke-width="1.5">
          <circle cx="31" cy="31" r="29"/>
          <path d="M20 38 C24 44 36 46 42 38 L42 24 M36 37 L36 20 M30 37 L30 18 M24 38 L24 24"/>
        </svg>
        <div class="feature-label">Ergonomic</div>
      </div>

      <div class="feature feature--quiet">
        <svg viewBox="0 0 62 62" fill="none" stroke="#fff" stroke-width="1.5">
          <circle cx="31" cy="31" r="29"/>
          <path d="M22 26 H28 L35 20 V42 L28 36 H22 Z"/>
          <path d="M18 18 L44 44"/>
        </svg>
        <div class="feature-label">Extremely quiet<br>&lt;45 dB</div>
      </div>

      <div class="feature feature--waterproof">
        <svg viewBox="0 0 62 62" fill="none" stroke="#fff" stroke-width="1.5">
          <circle cx="31" cy="31" r="29"/>
          <path d="M31 16 C26 25 22 30 22 36 A9 9 0 0 0 40 36 C40 30 36 25 31 16 Z" fill="#fff"/>
        </svg>
        <div class="feature-label">100% waterproof</div>
      </div>

      <div class="feature feature--luxurious">
        <svg viewBox="0 0 62 62" fill="none" stroke="#fff" stroke-width="1.5">
          <circle cx="31" cy="31" r="29"/>
          <path d="M19 26 L25 19 H37 L43 26 L31 44 Z M19 26 H43 M25 19 L31 26 L37 19 M31 26 V44"/>
        </svg>
        <div class="feature-label">Luxurious</div>
      </div>
    </aside>

    <section class="front-panel">
      <h1 class="brand-name">velmo</h1>
      <p class="product-type">Realastic Rabit Vibe</p>

      <div class="illustration-area" role="img" aria-label="Faint line illustration of an embracing couple"></div>
      <div class="product-image" role="img" aria-label="Purple rabbit vibrator with white base and power button"></div>

      <p class="tagline">Enjoi <span class="tagline-accent">Your</span> Passionate <span class="tagline-accent">Life</span></p>

      <div class="web-band">www.velmo.example</div>
    </section>
  </div>
</body>
</html>
```